Label for kLw Homestead beef tallow

I need a small label to go on a 2oz amber glass jar as well as a 4 oz. amber glass jar of moisturizer.
I prefer it to be rectangular for the 2oz jar since it's small and square for the 4oz jar.
I'd like to keep our kLw Homestead logo the same font and style, which is attached. Ten Sleep, Wyoming should be left out. The font for kLw Homestead is spartan.
The label content is as follows:
Heritage Tallow
Whipped Moisturizer
Ingredients: Beef Tallow, jojoba oil, peppermint oil.
2oz. jar

Instead of a white label, I'm thinking of a tan or brown label that will blend in with the amber jar. The lettering could then be a white, cream or even rust/burgandy color. Something to give it a rich look.

Thank you!

Target Market(s)

Mainly women but men as well.

Industry/Entity Type

Ranching and online beef sales

Requirements
Must have
• kLw Homestead logo

```html
<!DOCTYPE html>
<html lang="en">
<head>
<meta charset="utf-8">
<title>kLw Homestead – Heritage Tallow Labels</title>
<link href="https://fonts.googleapis.com/css2?family=League+Spartan:wght@400;500;600&family=Great+Vibes&display=swap" rel="stylesheet">
<style>
  :root {
    --backdrop: #e8e8e8;
    --label-paper: #ffffff;
    --ink: #0c0c0c;
    --band-text: #ffffff;
  }
  * { margin: 0; padding: 0; box-sizing: border-box; }
  html, body {
    width: 1200px;
    height: 1200px;
    overflow: hidden;
    background: var(--backdrop);
  }
  .canvas {
    position: relative;
    width: 1200px;
    height: 1200px;
    background: var(--backdrop);
    font-family: "League Spartan", Arial, sans-serif;
    color: var(--ink);
  }
  .label {
    position: absolute;
    background: var(--label-paper);
    border-radius: 36px;
    overflow: hidden;
  }

  /* 2 oz rectangular label */
  .label--small {
    left: 62px;
    top: 465px;
    width: 504px;
    height: 273px;
  }
  .label--small .side-band {
    position: absolute;
    left: 87px;
    top: 0;
    width: 35px;
    height: 100%;
    background: var(--ink);
  }
  .label--small .side-band .tagline {
    position: absolute;
    left: 50%;
    top: 50%;
    transform: translate(-50%, -50%) rotate(-90deg);
    white-space: nowrap;
    font-size: 26px;
  }
  .label--small .content {
    position: absolute;
    left: 130px;
    top: 17px;
    width: 274px;
    text-align: center;
  }
  .label--small .brand-mark { font-size: 112px; line-height: 0.9; }
  .label--small .brand-sub { font-size: 36px; line-height: 1.1; margin-top: 4px; }
  .label--small .product-name { font-size: 24px; font-weight: 500; margin-top: 28px; }
  .label--small .ingredients { font-size: 13.5px; font-weight: 500; margin-top: 4px; }
  .label--small .net-weight { font-size: 13px; font-weight: 500; margin-top: 12px; }

  /* 4 oz square label */
  .label--large {
    left: 634px;
    top: 348px;
    width: 503px;
    height: 503px;
  }
  .label--large .top-band {
    position: absolute;
    left: 0;
    top: 62px;
    width: 100%;
    height: 43px;
    background: var(--ink);
    display: flex;
    align-items: center;
    justify-content: center;
  }
  .label--large .top-band .tagline { font-size: 32px; }
  .label--large .content {
    position: absolute;
    left: 0;
    top: 128px;
    width: 100%;
    text-align: center;
  }
  .label--large .brand-mark { font-size: 150px; line-height: 0.88; }
  .label--large .brand-sub { font-size: 55px; line-height: 1.1; margin-top: 10px; }
  .label--large .product-name { font-size: 38px; font-weight: 500; margin-top: 36px; }
  .label--large .ingredients { font-size: 21px; font-weight: 500; margin-top: 6px; }
  .label--large .net-weight { font-size: 17px; font-weight: 500; margin-top: 22px; }

  .tagline {
    font-family: "Great Vibes", "Brush Script MT", cursive;
    color: var(--band-text);
    line-height: 1;
  }
  .brand-name { font-weight: 400; color: var(--ink); }
  .brand-mark, .brand-sub { display: block; }
  .product-name { letter-spacing: 0.01em; line-height: 1.1; }
  .ingredients, .net-weight { line-height: 1.1; }
</style>
</head>
<body>
<main class="canvas">

  <section class="label label--small" aria-label="2 oz jar label">
    <div class="side-band"><span class="tagline">Heritage Tallow</span></div>
    <div class="content">
      <p class="brand-name"><span class="brand-mark">kLw</span><span class="brand-sub">HOMESTEAD</span></p>
      <h2 class="product-name">WHIPPED MOISTURIZER</h2>
      <p class="ingredients">Beef Tallow, jojoba oil, peppermint oil</p>
      <p class="net-weight">2oz.</p>
    </div>
  </section>

  <section class="label label--large" aria-label="4 oz jar label">
    <div class="top-band"><span class="tagline">Heritage Tallow</span></div>
    <div class="content">
      <p class="brand-name"><span class="brand-mark">kLw</span><span class="brand-sub">HOMESTEAD</span></p>
      <h2 class="product-name">WHIPPED MOISTURIZER</h2>
      <p class="ingredients">Beef Tallow, jojoba oil, peppermint oil</p>
      <p class="net-weight">4oz.</p>
    </div>
  </section>

</main>
</body>
</html>
```